Mobile Repair Service on location needs a Web Design

We are starting a new mobile device repair service called Gadget Haven and our website needs a design!

Hello Designers!
First, we'd like to make clear this is more than a simple web design contest, we want the designers to create an idea. We want someone who can create the whole theme of the service's we provide. We want someone that can help design our visual branding, help us communicate a sentiment. And we are willing to pay for that.

Who are we?
Our company is based in Rotterdam, the Netherlands. We provide different services for all kinds of electronic devices. The kind of services we provide are, among other things, installations of hardware and software and the repair of broken or malfunctioning devices.
We are starting a new service that offers mobile device repairs on location, be it at the home of our customers, their office, or any other place. Just give us the address and we will come to you for the repair job. This is also our main USP. We have multiple skilled engineers who drive trough the country on a daily basis and can be on location within a working day. Repair is done immediately onsite while the customer waits. At this stage we will start with the smartphone product-group within the mobile devices. In a second phase we might also add tablets.
People don't want to be without their phone for weeks because of some parts that needed to be ordered by a repair center they had to sent their phone to. We offer a fully functional mobile repair center in the form of specially customized vans. These vans have all the tools and utilities needed by our engineers to safely repair your mobile device. Your phone is being repaired directly in front of you, the next business-day, on a location you desire.

For this new service we are creating a website called Gadget Haven. The website needs a story and matching design and this is where you come in. We are not looking for a simple template design we can get from any place. We need a story. We want you to create an idea, build a unique theme or vision that helps sell the product/service. This goes beyond the design of the website. We need the whole package, the design you are creating needs to have returning elements like icons, color use, images, maybe even characters etc. You name it! There needs to be a common thread in the design so we can reuse elements in, for example, the email templates, the work order or receipt we give to our customers (we may contact the winner of the contest to design these for us as well!).

The name 'Gadget Haven' is chosen. Haven (short for rehabilitate) has a bold and playful tone to it and the design needs to reflect the name. So we're looking for a somewhat playful and cheeky design. Definitely not too serious and definitely modern. We already got a logo that we love and that fit's this description (see attached design documents for the logo). It's bold, powerful and fun. Our web design needs to reflect this as well and has to fit in with our logo.
We would really like it if the design somehow incorporates elements that highlight our unique selling points (repairs on location, we come to you etc.). We would really like some form of story telling in the design. Think clumsy people breaking their phones. Teenagers in tears because they have no access to their friends. People nowadays have the need to always be 'connected'. What happens when your phone is broken or malfunctioning? We're handling tech, we are nerds and a little bit weird, but we're professionals and here to help you with your problem. The sentiment Wire Troop tries to communicate is something we really like. We're looking for fresh idea's, anything goes!

In an overview all Unique Selling Points of the Gadget haven service:
- Professional service on location. Don’t ship to us we will come to you!
- Clear pricing upfront. No hidden cost.
- Next business-day repair.
- Backed by a professional call center open 12 hours a day and open on a Saturday as well
- Backed by a professional repair center with more then 12 years of experience
- Repair is done by certified engineers
- 1 year warranty on the repair

The process:
The main function of our website will be for customers to make a repair request. A customer will visit our website and can make a repair request immediately by going through a 'request-order-flow'. In this flow he or she will need to fill in some forms and can select wich type/model/brand of mobile device he or she has and what parts need to be repaired. After a request is placed we will call the customer back (within an hour) for a short intake and to set a date/time and location. Our engineer will meet the customer at the specified location and will repair the device onsite in one of our mobile repair centers, which is a specialized van equipped with all the tools needed for device restorations.
So in short the steps are:
- Choose your device and repair job
- Place the order
- Get a callback within the hour
- Set date and location
- We will come to you.

Website functionality:
Our website is our main form of communication. So the sentiment we want to communicate needs be reflected in the design. We need a main/front page designed (preferably a long scrolling page design) containing:
1. Customers will be able to request a repair job directly on our website. So there will need to be a prominent button/link at the top of our main page that will bring the customer to this 'request-order-flow'. This is the main flow which needs to be full focus on the front page. All other items are secondary.
2. The general information of who we are and what we do, and why the customer should choose us. Preferably in short bullet-point type keywords/sentences with icons or other visual cues. See our unique selling points to get an idea of the information that will be displayed here.
3. There needs to be a section that will explain the process (see above) of a repair request step-by- step, again in brief short key sentences and with (custom) icons.
4. There needs to be a section that explains to the customer he/she can always contact us if they are not sure what the problem is with their device, and for this reason are not sure what repair request they should order.
5. We want to implement some functionality that display customer ratings or customer reviews. So there needs to be room for some kind of widget of plugin we're going to implement which shows these reviews.
6. A 'For business section' where we will explain all the options we provide for corporate clients.
7. Social media links.
8. There needs to be a menu with buttons that leads to the all sections described in the previous points.

For now, we need a design for our front page. In the second phase, when we have picked our winner, we may ask the winner to design the page(s) for our request workflow as well.

EDIT:
Finally, we have a very specific order in mind for the different segments of our website. We would like you to add some more segments that were not in our original brief as well:

1. Top header with order/request button. (should instantly make clear our main USP, we do repairs on location)
2. Our process
3. Our unique selling points / why choose us
4. The kind of repairs we do (broken screens, broken batteries, water damage, broken camera's, no sound etc.)
5. A 'meet our team' section, where we introduce some of our engineers
6. A 'contact us for any questions' section/
7. Testimonials/user reviews
8. A section where we show key performance indicators
9. 'For businesses' sections
10.'Subscribe for newsletter' field
11. Social media buttons

Industry/Entity Type

It Service

Number of Pages Required

1 page

Font styles to use
Sans Serif

Requirements
Must have
• a main/front page, design only
• custom icons/images for banners, adverts online and in print (high res)
Nice to have
• Storytelling in our design.
• Design that fits with our brand new logo.
• Elements like icons to have a flat design.
• Keep in mind that the website will need to be responsive when designing! (Ideally provide an example of the mobile design as well)
• Create a fun and trustworthy feeling.

```html
<!DOCTYPE html>
<html lang="en">
<head>
<meta charset="utf-8">
<title>Gadget Haven</title>
<link href="https://fonts.googleapis.com/css2?family=Open+Sans:wght@400;600&display=swap" rel="stylesheet">
<style>
:root{
  --ink:#333;
  --muted:#6f6f6f;
  --orange:#f26a3c;
  --blue:#2aa6d9;
  --blue-dark:#1f93c6;
  --lavender:#c5c3e8;
  --purple-a:#8e8bd2;
  --purple-b:#6c69b4;
  --pale:#eef4f9;
  --line:#cfd6dc;
  --white:#fff;
}
*{box-sizing:border-box;margin:0;padding:0}
html,body{width:1200px;height:2719px;overflow:hidden}
body{font-family:"Open Sans",Arial,sans-serif;color:var(--ink);background:var(--white);position:relative}
.abs{position:absolute}

/* header */
.brand{display:flex;align-items:center;gap:12px}
.brand-dot{width:44px;height:44px;border-radius:50%;background:var(--orange);flex:none}
.brand-name{font-weight:600;font-size:26px;line-height:1.05;color:var(--ink);text-transform:uppercase}
.top-info{font-size:13px;line-height:20px;color:var(--ink)}
.social{display:flex;gap:8px}
.social span{display:block;width:22px;height:22px;background:var(--blue);border-radius:3px}
.social.dark span{width:24px;height:24px;background:#555}

/* nav */
.nav{top:105px;left:0;width:1200px;height:60px;border:1px solid #ddd;display:flex;align-items:center}
.nav a{position:absolute;font-size:15px;color:var(--ink);text-decoration:none;transform:translateX(-50%);top:19px}
.nav a.active{color:var(--blue)}
.nav .book{left:905px;top:0;transform:none;width:205px;height:58px;background:var(--lavender);color:var(--white);display:flex;align-items:center;justify-content:center}

/* hero */
.hero{top:165px;left:0;width:1200px;height:509px;background:linear-gradient(135deg,#39b6e6,var(--blue) 50%,var(--blue-dark))}
.hero h1{position:absolute;left:107px;top:190px;font-weight:400;font-size:56px;color:var(--white);letter-spacing:1px}
.hero p{position:absolute;left:107px;top:253px;width:460px;font-size:22px;line-height:26px;color:var(--white)}
.hero .arrow{position:absolute;top:358px;width:28px;height:28px;border-radius:50%;background:#1d5f86}
.hero-visual{left:685px;top:0;width:403px;height:509px;background:linear-gradient(90deg,#e9ecef,#5a6068 55%,#2a2d31)}

/* welcome */
.van{left:82px;top:758px;width:444px;height:257px;background:linear-gradient(180deg,#f3f3f3,#d8d8d8);border-radius:30px 60px 20px 20px}
.welcome h2,.section-title{font-weight:400;font-size:29px;color:var(--ink);text-transform:uppercase}
.welcome h2{position:absolute;left:620px;top:752px}
.welcome p{position:absolute;left:620px;top:800px;width:490px;font-size:13.5px;line-height:22.7px;text-align:justify;color:#555}
.btn-outline{left:620px;top:977px;width:125px;height:33px;border:1.5px solid var(--orange);border-radius:17px;color:var(--orange);font-size:13.5px;display:flex;align-items:center;justify-content:center}

/* process */
.process{top:1097px;left:0;width:1200px;height:404px;background:linear-gradient(160deg,var(--purple-a),var(--purple-b))}
.process h2{position:absolute;top:60px;width:100%;text-align:center;font-weight:400;font-size:31px;color:var(--white)}
.step{position:absolute;top:154px;width:220px;transform:translateX(-50%);text-align:center;color:var(--white)}
.step .num{margin:0 auto;width:86px;height:86px;border:2px solid var(--white);border-radius:50%;font-size:30px;display:flex;align-items:center;justify-content:center}
.step p{margin-top:28px;font-size:14px;line-height:24px;text-transform:uppercase}
.step-arrow{position:absolute;top:184px;width:30px;height:26px}

/* what we do */
.whatwedo .section-title{position:absolute;left:91px;top:1606px;font-size:32px}
.usp{position:absolute;left:91px;top:1665px;list-style:none;font-size:15px;line-height:28.6px;color:#444}
.usp li::before{content:"\00BB";margin-right:8px;color:#555}
.mascot{left:743px;top:1532px;width:327px;height:404px;background:radial-gradient(circle at 50% 40%,#f7d9b0,var(--orange) 70%);border-radius:50% 50% 50% 50%/45% 45% 55% 55%}

/* about + contact */
.info{top:1973px;left:0;width:1200px;height:429px;background:var(--pale)}
.about-title{position:absolute;left:89px;top:2064px;font-size:25px}
.about-text{position:absolute;left:89px;top:2114px;width:466px;font-size:13.5px;line-height:22px;color:var(--muted);text-align:justify}
.contact-title{position:absolute;left:642px;top:2064px;font-size:25px}
.field{position:absolute;background:var(--white);border:1.5px solid var(--line);border-radius:3px;font-size:12px;color:#555;padding:14px 14px}
.btn-submit{left:1013px;top:2302px;width:98px;height:35px;border-radius:18px;background:var(--orange);color:var(--white);font-size:16px;display:flex;align-items:center;justify-content:center}

/* footer */
.footer-head{font-size:15px;color:var(--ink);text-transform:uppercase}
.footer-text{font-size:12px;line-height:29px;color:#555}
.mail-input{left:638px;top:2554px;width:147px;height:31px;border:1px solid var(--line);font-size:12px;padding:7px 8px;color:#555}
.mail-btn{left:785px;top:2554px;width:56px;height:31px;background:var(--blue);color:var(--white);font-size:12px;display:flex;align-items:center;justify-content:center}
.rule{left:74px;top:2647px;width:1050px;height:1px;background:#ccc}
.copyright{top:2671px;left:0;width:1200px;text-align:center;font-size:12px;color:#333}
</style>
</head>
<body>

<header>
  <div class="abs brand" style="left:92px;top:18px">
    <span class="brand-dot"></span>
    <span class="brand-name">Gadget<br>Haven</span>
  </div>
  <svg class="abs" style="left:515px;top:36px" width="30" height="30" viewBox="0 0 30 30" aria-hidden="true">
    <circle cx="15" cy="15" r="12" fill="none" stroke="#f26a3c" stroke-width="3"/>
    <path d="M15 8v8h6" fill="none" stroke="#f26a3c" stroke-width="2.5"/>
  </svg>
  <div class="abs top-info" style="left:557px;top:28px">Monday - Friday 08:00 - 20:00<br>Saturday and Sunday - CLOSED</div>
  <svg class="abs" style="left:798px;top:34px" width="20" height="32" viewBox="0 0 20 32" aria-hidden="true">
    <rect x="2" y="2" width="16" height="28" rx="3" fill="none" stroke="#f26a3c" stroke-width="3"/>
    <circle cx="10" cy="25" r="1.8" fill="#f26a3c"/>
  </svg>
  <div class="abs top-info" style="left:829px;top:28px">+ 603-555-0142<br>hello@gadgethaven.example</div>
  <div class="abs social" style="left:995px;top:32px"><span></span><span></span><span></span><span></span></div>
</header>

<nav class="abs nav">
  <a class="active" style="left:147px">HOME</a>
  <a style="left:281px">ABOUT US</a>
  <a style="left:419px">SERVICES</a>
  <a style="left:566px">PRODUCTS</a>
  <a style="left:702px">BRANDS</a>
  <a style="left:825px">DEALS</a>
  <a class="book">BOOK APPOINTMENT</a>
</nav>

<section class="abs hero">
  <h1>GADGET HAVEN</h1>
  <p>Neque porro quisquam est qui ipsum quia dolor sit amet consectetur</p>
  <span class="arrow" style="left:107px"></span>
  <span class="arrow" style="left:144px"></span>
  <svg class="abs" style="left:107px;top:358px" width="66" height="28" viewBox="0 0 66 28" aria-hidden="true">
    <path d="M17 8l-6 6 6 6M48 8l6 6-6 6" fill="none" stroke="#fff" stroke-width="2.5"/>
  </svg>
  <div class="abs hero-visual" role="img" aria-label="Two smartphones side by side, one intact and one with a cracked screen"></div>
</section>

<section class="welcome">
  <div class="abs van" role="img" aria-label="White branded service van for on-location repairs"></div>
  <h2>Welcome to Gadget Haven</h2>
  <p>Our company is based in Rotterdam, the Netherlands. We provide different services for all kinds of electronic devices. The kind of services we provide are, among other things, installations of hardware and software and the repair of broken or malfunctioning devices. We are starting a new service that offers mobile device repairs on location, be it at the home of our customers, their office, or any other place. Just give us the address and we will come to you for the repair job. This is also our main USP. We have multiple skilled</p>
  <div class="abs btn-outline">Read More &raquo;</div>
</section>

<section class="abs process">
  <h2>HOW IT WORK</h2>
  <div class="step" style="left:181px"><div class="num">1</div><p>Choose your<br>device and repair job</p></div>
  <div class="step" style="left:410px"><div class="num">2</div><p style="margin-top:40px">Place the order</p></div>
  <div class="step" style="left:620px"><div class="num">3</div><p>Get a callback<br>within the hour</p></div>
  <div class="step" style="left:830px"><div class="num">4</div><p>Set date and<br>location</p></div>
  <div class="step" style="left:1041px"><div class="num">5</div><p>We will come<br>to you.</p></div>
  <svg class="step-arrow" style="left:288px" viewBox="0 0 30 26" aria-hidden="true"><path d="M4 24V16q0-6 8-6h10V4l8 9-8 9v-6H12q-4 0-4 4v4z" fill="#fff"/></svg>
  <svg class="step-arrow" style="left:505px" viewBox="0 0 30 26" aria-hidden="true"><path d="M4 24V16q0-6 8-6h10V4l8 9-8 9v-6H12q-4 0-4 4v4z" fill="#fff"/></svg>
  <svg class="step-arrow" style="left:707px" viewBox="0 0 30 26" aria-hidden="true"><path d="M4 24V16q0-6 8-6h10V4l8 9-8 9v-6H12q-4 0-4 4v4z" fill="#fff"/></svg>
  <svg class="step-arrow" style="left:917px" viewBox="0 0 30 26" aria-hidden="true"><path d="M4 24V16q0-6 8-6h10V4l8 9-8 9v-6H12q-4 0-4 4v4z" fill="#fff"/></svg>
</section>

<section class="whatwedo">
  <h2 class="section-title">What we do</h2>
  <ul class="usp">
    <li>Professional service on location. Don’t ship to us we will come to you!</li>
    <li>Clear pricing upfront. No hidden cost.</li>
    <li>Next business-day repair.</li>
    <li>Backed by a professional call center open 12 hours a day and open on a Saturday as</li>
    <li>Backed by a professional repair center with more then 12 years of experience</li>
    <li>Repair is done by certified engineers</li>
    <li>1 year warranty on the repair</li>
  </ul>
  <div class="abs mascot" role="img" aria-label="Flat illustration of a hand holding a wrench over a phone inside a location pin"></div>
</section>

<section class="abs info"></section>
<h2 class="section-title about-title">About us</h2>
<p class="about-text">For this new service we are creating a website called Gadget Haven. The website needs a story and matching design and this is where you come in. We are not looking for a simple template design we can get from any place. We need a story. We want you to create an idea, build a unique theme or vision that helps sell the product/service. This goes beyond the design of the website. We need the whole package, the design you are creating needs to have returning elements like icons, color use, images, maybe even characters etc. You name it! There needs to be a common thread</p>
<h2 class="section-title contact-title">Contact form</h2>
<div class="field" style="left:644px;top:2118px;width:228px;height:50px">Name</div>
<div class="field" style="left:885px;top:2118px;width:228px;height:50px">Email id</div>
<div class="field" style="left:644px;top:2179px;width:228px;height:51px">Phone</div>
<div class="field" style="left:885px;top:2179px;width:228px;height:51px">Subject</div>
<div class="field" style="left:644px;top:2239px;width:469px;height:50px">Message</div>
<div class="abs btn-submit">SUBMIT</div>

<footer>
  <div class="abs brand" style="left:94px;top:2518px">
    <span class="brand-dot"></span>
    <span class="brand-name">Gadget<br>Haven</span>
  </div>
  <div class="abs" style="left:352px;top:2476px">
    <h3 class="footer-head" style="font-weight:400">Contact us</h3>
    <p class="footer-text" style="margin-top:10px">Address : Suite 12 Harbour Lane<br>Lakeside, Victoria 3999 Australia<br>Phone : +1300 555 019<br>Email : hello@gadgethaven.example</p>
  </div>
  <div class="abs" style="left:638px;top:2476px">
    <h3 class="footer-head" style="font-weight:400">Join our mailing list</h3>
    <p style="font-size:12px;line-height:17px;color:#444;margin-top:12px;width:200px">Your about us information would fit here nicely.</p>
  </div>
  <div class="abs mail-input">Email address</div>
  <div class="abs mail-btn">Submit</div>
  <div class="abs" style="left:923px;top:2476px">
    <h3 class="footer-head" style="font-weight:400">Follow us out there</h3>
  </div>
  <div class="abs social dark" style="left:925px;top:2521px;gap:14px"><span></span><span></span><span></span><span></span></div>
  <div class="abs rule"></div>
  <p class="abs copyright">Copyright © 2017. All Rights Reserved</p>
</footer>

</body>
</html>
```